Agriculture Technology Website Design Project

We need a new website for a company called Crest Yield Networks. We have a document laid out with all of the requirements (see below) and would like you to follow the instructions on there. In this document, there is all of the copy that must be included on the website and what order it should go in as well as images. These images have specific names and are listed in the document as to where they should go. Please make this one continuous site that users can easily scroll through. We would like it to be sleek and modern with as little clutter as possible. Please refer to the brochure that we have posted below (Brook Metrics.pdf) for a design we have had done for the company in the past. We really like this design and it would be great if the color scheme was similar on the website.

Industry/Entity Type

Agriculture

Number of Pages Required

1 page

Font styles to use
Sans Serif

```html
<!DOCTYPE html>
<html lang="en">
<head>
<meta charset="utf-8">
<title>Crest Yield Networks</title>
<link href="https://fonts.googleapis.com/css2?family=Poppins:wght@300;400;500;600;700&display=swap" rel="stylesheet">
<style>
:root{
  --green:#2b7a10;
  --green-dark:#1f6408;
  --green-light:#a9d18e;
  --green-pale:#e7f2dc;
  --card:#eef5e8;
  --ink:#222;
  --muted:#666;
  --white:#fff;
  --night:#1a2216;
}
*{margin:0;padding:0;box-sizing:border-box}
html,body{width:1200px;height:5310px;overflow:hidden}
body{font-family:'Poppins',sans-serif;color:var(--ink);background:var(--white);position:relative}
.abs{position:absolute}
.photo{position:absolute}
.hero{left:0;top:0;width:1200px;height:620px;background:linear-gradient(180deg,#2c3a2a 0%,#3e5236 45%,#26331f 100%)}
.brand{left:74px;top:18px;width:160px;text-align:center}
.brand-dot{width:26px;height:26px;border-radius:50%;background:var(--green);margin:0 auto 6px}
.brand-name{font-size:11px;font-weight:500;color:var(--green-light);letter-spacing:.5px}
.nav{top:0;left:560px;display:flex;gap:0;height:80px;align-items:flex-start}
.nav a{color:var(--white);text-decoration:none;font-size:14px;font-weight:400;padding:34px 10px 0;display:block}
.nav a.active{background:var(--green);border-radius:0 0 48px 48px;width:94px;height:74px;text-align:center;padding-top:34px}
.hero-title{left:0;width:1200px;top:240px;text-align:center;color:var(--white);font-size:50px;font-weight:700;letter-spacing:1px}
.hero-title span{color:var(--green)}
.hero-sub{left:0;width:1200px;top:308px;text-align:center;color:var(--white);font-size:17px}
.btn{position:absolute;background:var(--green);color:var(--white);font-size:19px;font-weight:500;border-radius:26px;text-align:center;line-height:50px;height:50px;letter-spacing:.5px}
.center{left:0;width:1200px;text-align:center}
.h-white{color:var(--white);font-weight:500}
.h-green{color:var(--green);font-weight:500}
.para{font-size:14px;line-height:27px;color:var(--white)}
.para.dark{color:var(--muted)}
.feature-circle{width:116px;height:116px;border-radius:50%;background:var(--white);box-shadow:0 6px 16px rgba(0,0,0,.18);display:flex;align-items:center;justify-content:center}
.feature-label{font-size:15px;line-height:26px;text-align:center;color:var(--ink);font-weight:400}
.arrow{width:58px;height:58px;border-radius:50%;border:2px solid #bbb;display:flex;align-items:center;justify-content:center}
.arrow.right{border-color:var(--green)}
.module{width:220px;text-align:center}
.module-icon{width:114px;height:114px;border-radius:50%;background:var(--green);margin:0 auto;display:flex;align-items:center;justify-content:center}
.module-title{color:var(--green-dark);font-size:15px;line-height:26px;margin-top:36px;font-weight:500}
.module-title.dark{color:var(--ink)}
.module-text{font-size:13.5px;line-height:25px;color:var(--muted);margin-top:16px}
.quote-card{background:var(--card);width:324px;height:300px;padding:34px 34px}
.quote-mark{font-size:56px;color:var(--green);font-weight:700;line-height:40px;height:40px}
.quote-text{font-size:14px;line-height:27px;color:#555;margin-top:12px}
.quote-name{font-size:15px;color:var(--ink);margin-top:22px}
.footer{left:0;top:4740px;width:1200px;height:570px;background:linear-gradient(180deg,#2f3b27 0%,#1d2718 60%,#151c11 100%)}
.social{width:44px;height:44px;border-radius:50%;background:var(--green)}
.contact-box{left:208px;top:5041px;width:784px;height:104px;border:1px solid rgba(255,255,255,.6);display:flex}
.contact-cell{flex:1;display:flex;align-items:center;padding:0 26px;gap:18px;border-right:1px solid rgba(255,255,255,.6);color:var(--white);font-size:14px;font-weight:600;line-height:24px}
.contact-cell:last-child{border-right:none}
.footer-links{top:5186px;color:var(--white);font-size:14px;font-weight:600}
.copy{top:5222px;color:var(--white);font-size:14px}
</style>
</head>
<body>

<!-- Hero -->
<div class="photo hero" role="img" aria-label="Sprinklers irrigating a field of crops at dusk"></div>
<div class="abs brand"><div class="brand-dot"></div><div class="brand-name">CREST YIELD NETWORKS</div></div>
<nav class="abs nav">
  <a class="active">HOME</a><a>ABOUT US</a><a>WHY CYN ?</a><a>MODULES</a><a style="margin-left:16px">PARTNERS</a><a>CONTACT US</a>
</nav>
<h1 class="abs hero-title">CREST <span>YIELD</span> NETWORKS</h1>
<p class="abs hero-sub">Bringing industrial automation to the farm</p>
<div class="btn" style="left:507px;top:355px;width:186px">CONTACT US</div>

<!-- Green brand band -->
<svg class="abs" style="left:0;top:520px" width="1200" height="460" viewBox="0 0 1200 460">
  <path d="M0 80 C250 0 950 0 1200 60 L1200 430 C900 360 300 360 0 440 Z" fill="#2b7a10"/>
</svg>
<div class="abs center" style="top:592px;display:flex;justify-content:center;align-items:center;gap:14px">
  <span style="width:14px;height:14px;border-radius:50%;background:#fff;display:inline-block"></span>
  <span style="color:#fff;font-size:40px;font-weight:300;line-height:1">Brook Metrics</span>
</div>
<h2 class="abs center h-white" style="top:686px;font-size:40px">BROOK METRICS</h2>
<p class="abs center para" style="top:750px;left:260px;width:680px">Brook Metrics is a cost-effective suite of tools built by Crest Yield Networks for irrigation management, providing farmers access to state-of-the-art industrial monitoring and control tools already widely adopted in other industries</p>

<div class="abs feature-circle" style="left:309px;top:864px"><svg width="54" height="54" viewBox="0 0 54 54"><rect x="6" y="6" width="42" height="42" rx="3" fill="none" stroke="#2b7a10" stroke-width="3"/><path d="M14 38 L24 26 L30 32 L40 18" fill="none" stroke="#2b7a10" stroke-width="3"/></svg></div>
<div class="abs feature-circle" style="left:536px;top:864px"><svg width="58" height="50" viewBox="0 0 58 50"><rect x="3" y="4" width="52" height="42" rx="3" fill="none" stroke="#2b7a10" stroke-width="3"/><line x1="3" y1="13" x2="55" y2="13" stroke="#2b7a10" stroke-width="3"/><circle cx="29" cy="30" r="8" fill="none" stroke="#2b7a10" stroke-width="3"/></svg></div>
<div class="abs feature-circle" style="left:787px;top:864px"><svg width="50" height="56" viewBox="0 0 50 56"><rect x="4" y="3" width="42" height="50" rx="4" fill="none" stroke="#2b7a10" stroke-width="3"/><line x1="4" y1="14" x2="46" y2="14" stroke="#2b7a10" stroke-width="3"/><circle cx="25" cy="34" r="11" fill="none" stroke="#2b7a10" stroke-width="3"/></svg></div>
<div class="abs feature-label" style="left:277px;top:993px;width:180px">REMOTE CROP<br>MONITORING</div>
<div class="abs feature-label" style="left:474px;top:998px;width:240px">REMOTE PUMP<br>MONITORING &amp; CONTROL</div>
<div class="abs feature-label" style="left:755px;top:993px;width:180px">IRRIGATION<br>AUTOMATION</div>

<!-- Irrigation automation -->
<h2 class="abs center h-green" style="top:1080px;font-size:35px;line-height:46px">WHAT IS IRRIGATION<br>AUTOMATION?</h2>
<div class="photo" style="left:301px;top:1192px;width:594px;height:354px;background:linear-gradient(180deg,#8fb7dc 0%,#c9d9e4 35%,#a8a39a 60%,#8a7a60 100%)" role="img" aria-label="Irrigation filter station and pump equipment on a farm"></div>
<div class="abs arrow" style="left:202px;top:1346px"><svg width="14" height="22"><path d="M11 2 L3 11 L11 20" fill="none" stroke="#999" stroke-width="2"/></svg></div>
<div class="abs arrow right" style="left:924px;top:1346px"><svg width="14" height="22"><path d="M3 2 L11 11 L3 20" fill="none" stroke="#2b7a10" stroke-width="2"/></svg></div>
<p class="abs center para dark" style="top:1570px;left:290px;width:620px">Brook Metrics Irrigation Automation includes both valve and pump control systems that brings best-in-class industrial control technology to agriculture to provide farmers with cost-effective, easy-to-use solutions. Brook Metrics provides the flexibility and remote control to support precise delivery of plant-water needs with a significant reduction in irrigation labor requirements, making it the most powerful solution in the industry.</p>
<svg class="abs" style="left:0;top:1680px" width="1200" height="200" viewBox="0 0 1200 200">
  <path d="M0 60 C200 170 700 170 1200 60 L1200 110 C800 200 300 200 0 185 Z" fill="#e7f2dc"/>
  <path d="M0 110 C300 190 800 170 1200 120 L1200 140 C800 200 300 200 0 185 Z" fill="#a9d18e"/>
</svg>

<!-- Integrator -->
<h2 class="abs h-green" style="left:99px;top:1952px;font-size:40px;line-height:44px">CYN IS SYSTEMS<br>INTEGRATOR</h2>
<p class="abs" style="left:102px;top:2064px;font-size:16px;line-height:28px;width:420px">OUR GOAL: To Be your Trusted Partner for Technology Adoption</p>
<p class="abs para dark" style="left:102px;top:2133px;width:440px">Our focus is on helping California growers design, build and adopt effective irrigation management solutions.Our team has worked together for over 15 years, providing monitoring and control systems for 60+ crops that have successfully helped</p>
<p class="abs para dark" style="left:102px;top:2282px;width:440px">Over 500 farms significantly improve irrigation manage - ment. We also farm our own 200 acre technology lab to help ensure we deliver reliable monitoring &amp; automation to your farm.</p>
<div class="btn" style="left:99px;top:2412px;width:165px">MODULES</div>
<svg class="abs" style="left:770px;top:1940px" width="360" height="360"><circle cx="180" cy="180" r="158" fill="none" stroke="#d9ebcb" stroke-width="26"/></svg>
<div class="photo" style="left:639px;top:1963px;width:285px;height:305px;background:linear-gradient(160deg,#5d7a3a,#2f4a1c)" role="img" aria-label="Almond tree branches with green nuts"></div>
<div class="photo" style="left:786px;top:2140px;width:284px;height:316px;background:linear-gradient(180deg,#9bbad6 0%,#7da048 40%,#8a7a5a 100%)" role="img" aria-label="Young orchard tree in a field"></div>

<!-- Why -->
<svg class="abs" style="left:0;top:2660px" width="240" height="380"><path d="M0 8 A185 185 0 0 1 0 372" fill="none" stroke="#d9ebcb" stroke-width="30" transform="translate(-150 0)"/><circle cx="20" cy="190" r="170" fill="none" stroke="#d9ebcb" stroke-width="28"/></svg>
<div class="photo" style="left:126px;top:2600px;width:443px;height:332px;background:linear-gradient(180deg,#9cc3e6 0%,#b7a68a 35%,#5c7d36 55%,#3f5f22 100%)" role="img" aria-label="Vineyard rows in front of mountains"></div>
<h2 class="abs h-green" style="left:678px;top:2602px;font-size:40px">WHY CYN?</h2>
<p class="abs" style="left:682px;top:2662px;font-size:16px">We're Your Local Crest Yield Team.</p>
<p class="abs para dark" style="left:682px;top:2710px;width:400px">We are experts at deploying Information Technology for irrigation management. We partner with our customers to deliver the right solutions. Everything we sell is off-the-shelf, cost-effective and reliable</p>
<div class="btn" style="left:680px;top:2866px;width:198px">GET IN TOUCH</div>

<!-- Modules -->
<svg class="abs" style="left:0;top:3040px" width="1200" height="100"><path d="M0 90 C300 10 900 0 1200 40 L1200 100 L0 100 Z" fill="#f1f8ea"/></svg>
<div class="abs" style="left:0;top:3120px;width:1200px;height:440px;background:linear-gradient(180deg,#f1f8ea 0%,#ffffff 40%)"></div>
<div class="abs" style="left:591px;top:3148px;width:22px;height:22px;border-radius:50%;background:var(--green)"></div>

<div class="abs module" style="left:69px;top:3246px">
  <div class="module-icon" style="box-shadow:0 0 0 4px #fff,0 0 0 6px #2b7a10"><svg width="54" height="50"><rect x="6" y="14" width="42" height="30" rx="3" fill="none" stroke="#fff" stroke-width="3"/><rect x="18" y="4" width="18" height="10" fill="none" stroke="#fff" stroke-width="3"/></svg></div>
  <div class="module-title">CHEMIGATION<br>AUTOMATION</div>
  <div class="module-text">Control of your fertilizer injection and monitor tank levels to optimize inputs.</div>
</div>
<div class="abs module" style="left:282px;top:3246px">
  <div class="module-icon"><svg width="50" height="50"><rect x="5" y="5" width="40" height="40" rx="3" fill="none" stroke="#fff" stroke-width="3"/><path d="M12 36 L22 24 L28 30 L38 16" fill="none" stroke="#fff" stroke-width="3"/></svg></div>
  <div class="module-title dark">CROP<br>MONITORING</div>
  <div class="module-text">Ensuring that you have real-time information to optimize irrigation management</div>
</div>
<div class="abs module" style="left:492px;top:3246px">
  <div class="module-icon"><svg width="54" height="46"><rect x="3" y="3" width="48" height="40" rx="3" fill="none" stroke="#fff" stroke-width="3"/><line x1="3" y1="12" x2="51" y2="12" stroke="#fff" stroke-width="3"/><circle cx="27" cy="28" r="7" fill="none" stroke="#fff" stroke-width="3"/></svg></div>
  <div class="module-title dark">PUMP MONITORING<br>&amp; CONTROL</div>
  <div class="module-text">Scalable and cost-effective pump monitoring with built-in remote control</div>
</div>
<div class="abs module" style="left:707px;top:3246px">
  <div class="module-icon"><svg width="46" height="54"><rect x="3" y="3" width="40" height="48" rx="4" fill="none" stroke="#fff" stroke-width="3"/><line x1="3" y1="13" x2="43" y2="13" stroke="#fff" stroke-width="3"/><circle cx="23" cy="32" r="10" fill="none" stroke="#fff" stroke-width="3"/></svg></div>
  <div class="module-title dark">IRRIGATION<br>AUTOMATION</div>
  <div class="module-text">Upgrade your irrigation system: from retrofit to ranch-wide automation</div>
</div>
<div class="abs module" style="left:917px;top:3246px">
  <div class="module-icon"><svg width="46" height="46" viewBox="0 0 24 24"><path d="M6.6 10.8a15 15 0 0 0 6.6 6.6l2.2-2.2a1 1 0 0 1 1-.25 11.4 11.4 0 0 0 3.6.6 1 1 0 0 1 1 1V20a1 1 0 0 1-1 1A17 17 0 0 1 3 4a1 1 0 0 1 1-1h3.5a1 1 0 0 1 1 1 11.4 11.4 0 0 0 .6 3.6 1 1 0 0 1-.25 1z" fill="none" stroke="#fff" stroke-width="1.4"/></svg></div>
  <div class="module-title dark" style="margin-top:48px">CONTACT US</div>
  <div class="module-text">For immediate support call (555 014 - 2290)</div>
</div>
<svg class="abs" style="left:1040px;top:3440px" width="160" height="380"><circle cx="200" cy="190" r="170" fill="none" stroke="#d9ebcb" stroke-width="28"/></svg>

<!-- Chemigation band -->
<svg class="abs" style="left:0;top:3620px" width="1200" height="560" viewBox="0 0 1200 560">
  <path d="M0 170 C300 40 900 20 1200 60 L1200 540 C900 470 300 480 0 490 Z" fill="#2b7a10"/>
</svg>
<h2 class="abs center h-white" style="top:3752px;font-size:29px">CHEMIGATION AUTOMATION</h2>
<p class="abs center para" style="top:3838px;left:190px;width:820px">Full scale fertilizer chemical injection system that automates fertigation and chemigation at critical times in your irrigation strategy. The system is set up to fertilize when your crop needs it the most. Along with pump and valve automation from your bulk tanks the system can monitor tank levels and record precise fertilizer delivery for each irrigation event and send critical alerts when tanks run low on material. Brook Metrics supports an unlimited number of variations of product and blending options depending on how you want to blend different products.</p>

<!-- Testimonials -->
<h2 class="abs center h-green" style="top:4166px;font-size:38px">WHAT OUR CLIENTS SAY</h2>
<div class="abs quote-card" style="left:76px;top:4247px"><div class="quote-mark">&ldquo;</div><p class="quote-text">Lorem Ipsum is simply dummy text of the printing and typesetting industry. Lorem Ipsum has been the industry's standard dummy text ever since the 1500.</p><p class="quote-name">- CLIENT NAME</p></div>
<div class="abs quote-card" style="left:439px;top:4247px"><div class="quote-mark">&ldquo;</div><p class="quote-text">Lorem Ipsum is simply dummy text of the printing and typesetting industry. Lorem Ipsum has been the industry's standard dummy text ever since the 1500.</p><p class="quote-name">- CLIENT NAME</p></div>
<div class="abs quote-card" style="left:800px;top:4247px"><div class="quote-mark">&ldquo;</div><p class="quote-text">Lorem Ipsum is simply dummy text of the printing and typesetting industry. Lorem Ipsum has been the industry's standard dummy text ever since the 1500.</p><p class="quote-name">- CLIENT NAME</p></div>

<!-- Footer -->
<div class="photo footer" role="img" aria-label="Sprinklers watering a crop field at night"></div>
<svg class="abs" style="left:0;top:4610px" width="1200" height="190" viewBox="0 0 1200 190">
  <path d="M0 10 C400 60 800 40 1200 0 L1200 70 C800 130 400 140 0 90 Z" fill="#d9ebcb"/>
  <path d="M0 90 C400 140 800 130 1200 70 L1200 0 L1200 130 L0 130 Z" fill="#ffffff" opacity="0"/>
  <path d="M0 90 C400 150 800 140 1200 70 L1200 130 C800 190 400 190 0 150 Z" fill="#ffffff"/>
</svg>
<div class="abs center" style="top:4840px;display:flex;justify-content:center;align-items:center;gap:14px">
  <span style="width:20px;height:20px;border-radius:50%;background:var(--green);display:inline-block"></span>
  <span style="color:var(--green);font-size:40px;font-weight:600;line-height:1">CYN</span>
</div>
<div class="abs social" style="left:522px;top:4960px"></div>
<div class="abs social" style="left:577px;top:4960px"></div>
<div class="abs social" style="left:632px;top:4960px"></div>

<div class="abs contact-box">
  <div class="contact-cell"><svg width="22" height="30" viewBox="0 0 22 30"><path d="M11 1C5.5 1 1 5.3 1 10.8 1 18 11 29 11 29s10-11 10-18.2C21 5.3 16.5 1 11 1z" fill="none" stroke="#3c9a18" stroke-width="2.4"/><circle cx="11" cy="11" r="3.5" fill="#3c9a18"/></svg><span>Lorem ipsum<br>simple<br>text print text.</span></div>
  <div class="contact-cell"><svg width="30" height="30" viewBox="0 0 24 24"><path d="M6.6 10.8a15 15 0 0 0 6.6 6.6l2.2-2.2a1 1 0 0 1 1-.25 11.4 11.4 0 0 0 3.6.6 1 1 0 0 1 1 1V20a1 1 0 0 1-1 1A17 17 0 0 1 3 4a1 1 0 0 1 1-1h3.5a1 1 0 0 1 1 1 11.4 11.4 0 0 0 .6 3.6 1 1 0 0 1-.25 1z" fill="#3c9a18"/></svg><span>Phone :<br>555 014 - 2290</span></div>
  <div class="contact-cell"><svg width="30" height="22" viewBox="0 0 30 22"><rect x="1" y="1" width="28" height="20" rx="2" fill="#3c9a18"/><path d="M2 3 L15 13 L28 3" fill="none" stroke="#1d2718" stroke-width="2"/></svg><span>Email :<br>info@crestyield.net</span></div>
</div>
<div class="abs center footer-links">Home &nbsp;| &nbsp;About &nbsp;| &nbsp;Why CYN? &nbsp;| &nbsp;Products &nbsp;&nbsp;&nbsp;&nbsp;&nbsp;&nbsp;&nbsp;&nbsp;&nbsp;&nbsp;&nbsp;| &nbsp;Partners &nbsp;| &nbsp;Contact</div>
<div class="abs center copy">&copy;CYN - 2020 All rights reserved.</div>

</body>
</html>
```